A start up special flyer design!

Hi All - Have updated the attachment content - This is the info required for the designs.
I need a catchy flyer to send out to a few areas to advertise the start of my plumbing business!
The flyer will contain an offer for customers, which will need to have some key details on it. See attached. Feel free to fit these criteria into the flyer given your knowledge on design and messaging principles. Key thing to get across to customers is the discount and special offer, and that it is a start up offer.
I have a logo that needs to be on the flyer as well - let me know what format you require and I will send through to you.
The color scheme needs to be blue / grey / black / white.
Let me know if you have any questions.
I

```html
<!DOCTYPE html>
<html lang="en">
<head>
<meta charset="utf-8">
<title>Reid Pipe Plumbing – Start Up Offer Flyer</title>
<link rel="stylesheet" href="https://fonts.googleapis.com/css2?family=Roboto+Condensed:wght@400;700;900&family=Roboto:wght@400;500;700&display=swap">
<style>
  :root {
    --blue: #1b6fd0;
    --blue-deep: #0d4fa8;
    --black: #151515;
    --charcoal: #2a2a2a;
    --grey-light: #eceef0;
    --grey-mid: #b9bec4;
    --fine: #cfd3d8;
    --white: #ffffff;
    --page: #d7dadd;
  }
  * { margin: 0; padding: 0; box-sizing: border-box; }
  html, body { width: 1000px; height: 1200px; overflow: hidden; }
  body { background: var(--page); font-family: "Roboto", Arial, sans-serif; }

  .flyer {
    position: absolute; left: 87px; top: 20px;
    width: 825px; height: 1160px; overflow: hidden;
    background: linear-gradient(180deg, #ffffff 0%, var(--grey-light) 60%, #e2e4e7 100%);
    box-shadow: 0 6px 24px rgba(0,0,0,.25);
  }
  .flyer-shapes { position: absolute; inset: 0; }

  .headline {
    position: absolute; left: 40px; top: 58px;
    font-family: "Roboto Condensed", Arial, sans-serif; font-weight: 900;
    text-transform: uppercase; line-height: 1;
  }
  .headline-lead { color: var(--black); font-size: 30px; line-height: 1.08; letter-spacing: .3px; }
  .headline-key { color: var(--blue); font-size: 62px; line-height: .98; margin-top: 8px; }
  .headline-key span { display: block; padding-left: 80px; }

  .brand {
    position: absolute; left: 60px; top: 430px;
    display: flex; align-items: center; gap: 14px;
    font-family: "Roboto Condensed", Arial, sans-serif; font-weight: 400;
    color: var(--blue); text-transform: uppercase;
  }
  .brand-mark { width: 16px; height: 16px; background: var(--blue); }
  .brand-name { font-size: 36px; letter-spacing: 1px; line-height: 1.05; }
  .brand-name small { display: block; font-size: 22px; letter-spacing: 6px; text-align: center; }

  .offer-tag {
    position: absolute; left: 505px; top: 510px; width: 255px; height: 96px;
    background: var(--black); color: var(--white);
    font-family: "Roboto Condensed", Arial, sans-serif; font-weight: 900;
    font-size: 62px; display: flex; align-items: center; justify-content: center;
    border-bottom: 6px solid var(--blue);
  }

  .deal { position: absolute; left: 54px; top: 630px; padding-left: 22px; border-left: 6px solid var(--grey-mid); }
  .deal-amount { color: var(--blue); font-weight: 700; font-size: 72px; line-height: 1; }
  .deal-amount b { font-size: 56px; }
  .deal-scope { color: var(--black); font-family: "Roboto Condensed", Arial, sans-serif; font-weight: 900; font-size: 46px; line-height: 1.05; text-transform: uppercase; }

  .perk {
    position: absolute; left: 60px; padding-left: 16px;
    border-left: 6px solid var(--grey-mid);
    font-weight: 700; font-size: 23px; line-height: 1.3; color: var(--charcoal);
  }
  .perk-gst { top: 790px; }
  .perk-check { top: 868px; }

  .booking { position: absolute; left: 50px; top: 988px; color: var(--white); }
  .booking-title { font-family: "Roboto Condensed", Arial, sans-serif; font-weight: 700; font-size: 30px; line-height: 1.2; text-transform: uppercase; }
  .booking-text { font-size: 17px; line-height: 1.35; margin-top: 4px; }
  .booking-text b { font-weight: 700; }

  .fine-print {
    position: absolute; right: 30px; top: 1016px; width: 300px;
    color: var(--fine); font-size: 10.5px; line-height: 1.45; text-align: right;
  }
  .contact {
    position: absolute; display: flex; align-items: center; gap: 12px;
    color: var(--white); font-weight: 700; line-height: 1;
  }
  .contact svg { flex: none; }
  .contact-web { right: 34px; top: 1074px; font-size: 20px; }
  .contact-phone { left: 56px; top: 1120px; font-size: 30px; font-family: "Roboto Condensed", Arial, sans-serif; letter-spacing: 1px; }
  .contact-mail { right: 34px; top: 1126px; font-size: 19px; font-weight: 500; }
</style>
</head>
<body>
<main class="flyer">
  <svg class="flyer-shapes" width="825" height="1160" viewBox="0 0 825 1160">
    <defs>
      <linearGradient id="photoTop" x1="0" y1="0" x2="1" y2="1">
        <stop offset="0" stop-color="#eef1f5"/>
        <stop offset="0.55" stop-color="#c3ccd6"/>
        <stop offset="1" stop-color="#6f88b0"/>
      </linearGradient>
      <linearGradient id="photoWorker" x1="0" y1="0" x2="0" y2="1">
        <stop offset="0" stop-color="#d9dde2"/>
        <stop offset="0.3" stop-color="#3a4a6a"/>
        <stop offset="1" stop-color="#1c2438"/>
      </linearGradient>
    </defs>

    <polygon class="photo-hero" role="img" aria-label="Photo of a smiling plumber fitting pipes under a sink"
             points="0,0 825,0 825,330 560,440 420,268 0,268" fill="url(#photoTop)"/>

    <polygon class="dark-wedge" points="0,268 420,268 560,440 300,545 0,520" fill="var(--black)"/>
    <polygon class="blue-sweep" points="300,545 825,325 825,392 395,545" fill="var(--blue)"/>
    <polygon class="white-line" points="395,545 825,392 825,400 418,545" fill="var(--white)"/>
    <polygon class="blue-sweep-thin" points="418,545 825,400 825,418 470,545" fill="var(--blue-deep)"/>

    <path class="photo-worker" role="img" aria-label="Photo of a plumber holding a hose, tap and wrench"
          d="M590,680 Q650,655 720,680 L770,740 L800,975 L548,975 L565,740 Z" fill="url(#photoWorker)"/>

    <polygon class="footer-band" points="0,975 560,975 600,1005 825,1005 825,1160 0,1160" fill="var(--black)"/>
    <polygon class="footer-accent" points="560,975 600,975 640,1005 600,1005" fill="var(--blue)"/>
    <polygon class="footer-strip" points="0,1110 825,1110 825,1160 0,1160" fill="var(--blue)"/>
    <polygon class="footer-notch" points="430,1110 490,1110 460,1160 400,1160" fill="var(--black)"/>
  </svg>

  <h1 class="headline">
    <div class="headline-lead">Delivering Quality<br>Work at a</div>
    <div class="headline-key">Decent<span>Price</span></div>
  </h1>

  <div class="brand">
    <span class="brand-mark"></span>
    <div class="brand-name">Reid Pipe<small>Plumbing</small></div>
  </div>

  <div class="offer-tag">OFFER</div>

  <section class="deal">
    <div class="deal-amount">15% <b>OFF</b></div>
    <div class="deal-scope">Your Overall Bill*</div>
  </section>

  <p class="perk perk-gst">No Gst Payable, Saving You<br>Additional 10% On Your Bill^</p>
  <p class="perk perk-check">Plus, A Free Hot Water<br>Health Check And<br>Replacement Quote~</p>

  <section class="booking">
    <h2 class="booking-title">To Make An Appointment</h2>
    <p class="booking-text"><b>Call Or Email</b> Reid,<br>Or Alternatively Make A Booking<br>Directly On The <b>Website</b></p>
  </section>

  <p class="fine-print">*Offer valid between 15 August 2016 to 15 October 2016<br>^Valid until 30 September 2016.<br>~Quote valid for 12 months from the quote date.</p>

  <div class="contact contact-web">
    <svg width="20" height="20" viewBox="0 0 20 20" fill="none" stroke="#fff" stroke-width="1.6"><circle cx="10" cy="10" r="8"/><ellipse cx="10" cy="10" rx="3.5" ry="8"/><path d="M2 10h16M3.5 6h13M3.5 14h13"/></svg>
    www.reidpipeplumbing.com
  </div>
  <div class="contact contact-phone">
    <svg width="28" height="28" viewBox="0 0 28 28" fill="none" stroke="#fff" stroke-width="2"><circle cx="14" cy="14" r="12"/><path d="M10 8l2 3-1.5 1.5a8 8 0 0 0 5 5L17 16l3 2-1 2.5c-5 0-11-6-11-11z" fill="#fff"/></svg>
    0491 570 228
  </div>
  <div class="contact contact-mail">
    <svg width="22" height="16" viewBox="0 0 22 16" fill="none" stroke="#fff" stroke-width="1.6"><rect x="1" y="1" width="20" height="14"/><path d="M1 1l10 8 10-8"/></svg>
    reid@reidpipeplumbing.com
  </div>
</main>
</body>
</html>
```